International Business Consulting Company Website

TW Harbor Advisory is a U.S-based international consulting firm. We combined passion for success in the global business arena with hands-on experience to help foreign companies navigate the entry into U.S. markets and U.S. companies in initiating and expanding exports to foreign markets.

We need a simple 1 page website
Examples of other consultants’ websites:
http://www.quillmarkadvisors.example/#intro
https://www.rtb-advisory.example
http://venmoragroup.example
https://brightfieldadvice.example

I also need the designer to suggest stock images that are suitable (related to international business, exports).

We want our web design to be bold, yet clean and simple.

Target Market(s)

US companies that export abroad, foreign companies that want to do business int he US/ open a subsidiary in the US.

Industry/Entity Type

Business Consultant

Coding

Coded - Design and coding required

Font styles to use
Sans Serif

Requirements
Must have
• Company logo on top

```html
<!DOCTYPE html>
<html lang="en">
<head>
<meta charset="utf-8">
<title>TW Harbor Advisory</title>
<link href="https://fonts.googleapis.com/css2?family=Lato:wght@400;700&family=Marcellus&display=swap" rel="stylesheet">
<style>
:root{
  --blue:#1450a3;
  --blue-dark:#0e3f86;
  --ink:#1d1d1d;
  --text:#333;
  --grey-band:#ececec;
  --white:#fff;
  --footer:#141414;
  --footer-deep:#0b0b0b;
  --line:#cfcfcf;
}
*{box-sizing:border-box;margin:0;padding:0}
html,body{width:1200px;height:3255px;overflow:hidden}
body{font-family:'Lato',sans-serif;color:var(--text);background:var(--white);position:relative}
.abs{position:absolute}

/* hero */
.hero{position:absolute;left:0;top:0;width:1200px;height:660px;
  background:radial-gradient(ellipse 320px 300px at 780px 330px,#8b9aa8 0%,#4a5866 40%,transparent 75%),
  linear-gradient(180deg,#1b232c 0%,#27313c 45%,#10161c 100%)}
.nav{position:absolute;top:62px;left:0;width:1200px;height:30px}
.nav a{position:absolute;top:8px;color:var(--white);text-decoration:none;font-size:14px;letter-spacing:.5px}
.nav .sep{position:absolute;top:6px;width:1px;height:16px;background:rgba(255,255,255,.45)}
.logo{position:absolute;left:463px;top:38px;display:flex;align-items:center;gap:12px}
.logo .mark{width:48px;height:48px;border:2px solid var(--white)}
.logo span{font-family:'Marcellus',serif;color:var(--white);font-size:27px;letter-spacing:1px;line-height:1}
.hero h1{position:absolute;left:100px;top:312px;font-family:'Lato',sans-serif;font-weight:400;color:var(--white);font-size:40px;letter-spacing:1px}
.hero .tag{position:absolute;left:100px;top:364px;color:var(--white);font-size:23px}

/* intro */
.intro{position:absolute;top:660px;left:0;width:1200px;height:215px;background:var(--grey-band);
  display:flex;align-items:center;justify-content:center}
.intro p{width:1010px;text-align:center;font-size:20px;line-height:32px;color:var(--ink)}

/* section title */
.section-title{position:absolute;left:0;width:1200px;text-align:center;font-family:'Marcellus',serif;font-size:35px;color:var(--ink);letter-spacing:.5px}
.section-title em{font-style:normal;color:var(--blue)}
.divider{position:absolute;left:375px;width:450px;height:20px}
.divider::before{content:"";position:absolute;left:0;right:0;top:9px;height:1px;background:var(--line)}
.divider::after{content:"";position:absolute;left:216px;top:1px;width:18px;height:18px;background:var(--white);border:1px solid #aaa}
.divider.on-grey::after{background:var(--grey-band)}

/* about */
.lead{position:absolute;top:1045px;left:0;width:1200px;text-align:center;color:var(--blue);font-weight:700;font-size:14.5px}
.about-intro{position:absolute;top:1082px;left:130px;width:940px;text-align:center;font-size:13.5px;line-height:22px}
.portrait{position:absolute;left:100px;top:1155px;width:335px;height:485px;background:#111;padding:9px}
.portrait div{width:100%;height:100%;border:1px solid #777;background:radial-gradient(ellipse 130px 160px at 50% 40%,#6e5a50 0%,#3a2e2a 55%,#141414 100%)}
.bio{position:absolute;left:474px;top:1206px;width:626px;font-size:13.2px;line-height:22.5px;color:var(--text)}
.bio p{margin-bottom:9px;text-align:justify}

/* services */
.services-band{position:absolute;top:1710px;left:0;width:1200px;height:175px;background:var(--grey-band)}
.panel{position:absolute;width:600px;height:485px}
.panel.blue{background:var(--blue);color:var(--white);padding:44px 42px 0 98px}
.panel h3{font-size:21px;line-height:29px;font-weight:400;letter-spacing:.3px}
.panel hr{border:0;border-top:1px solid rgba(255,255,255,.35);margin:18px 0 22px;width:460px}
.panel ul{list-style:none}
.panel li{position:relative;padding-left:34px;font-size:15.5px;line-height:21px;margin-bottom:11px}
.panel li::before{content:"";position:absolute;left:0;top:3px;width:15px;height:15px;border:1.5px solid rgba(255,255,255,.8)}
.photo-meeting{background:linear-gradient(135deg,#d9cdbb 0%,#a8886a 40%,#6d5a4c 70%,#cfc4b6 100%)}
.photo-tablet{background:linear-gradient(160deg,#9fb2c6 0%,#dde4eb 45%,#4c5561 80%,#b9c3cc 100%)}
.grey-gap{position:absolute;top:2855px;left:0;width:1200px;height:70px;background:var(--grey-band)}

/* footer */
.footer{position:absolute;top:2925px;left:0;width:1200px;height:280px;background:var(--footer);color:var(--white)}
.footer h4{position:absolute;top:33px;font-weight:400;font-size:16px;letter-spacing:1px}
.field{position:absolute;left:183px;width:275px;border:1px solid #8a8a8a;font-size:12px;color:#ddd;padding:7px 10px}
.send{position:absolute;left:183px;top:213px;width:86px;height:34px;background:var(--blue);color:var(--white);font-size:13px;text-align:center;line-height:34px;letter-spacing:1px}
.map{position:absolute;left:505px;top:72px;width:290px;height:175px;background:linear-gradient(135deg,#cfe0ea 0%,#b6cbd8 45%,#e4e7d8 100%)}
.contact{position:absolute;left:858px;font-size:13.5px;line-height:19px;color:#eee}
.contact svg{position:absolute;left:0;top:2px}
.contact span{display:block;padding-left:22px}
.social{position:absolute;top:210px;width:28px;height:28px;border:1px solid #bbb}
.copyright{position:absolute;top:3205px;left:0;width:1200px;height:50px;background:var(--footer-deep);color:#ccc;font-size:12px;text-align:center;line-height:50px}
</style>
</head>
<body>

<header class="hero" role="img" aria-label="Photo of a businessman in a suit holding small figures of people in cupped hands">
  <nav class="nav">
    <span class="sep" style="left:100px"></span>
    <a href="#" style="left:152px">HOME</a>
    <span class="sep" style="left:253px"></span>
    <a href="#" style="left:310px">ABOUT US</a>
    <span class="sep" style="left:430px"></span>
    <span class="sep" style="left:770px"></span>
    <a href="#" style="left:820px">OUR SERVICES</a>
    <span class="sep" style="left:950px"></span>
    <a href="#" style="left:978px">CONTACT US</a>
    <span class="sep" style="left:1100px"></span>
  </nav>
  <div class="logo"><div class="mark"></div><span>TW HARBOR ADVISORY</span></div>
  <h1>TW HARBOR ADVISORY</h1>
  <p class="tag">Market Entry &amp; Economic Development</p>
</header>

<section class="intro">
  <p>TW Harbor Advisory is a U.S-based international consulting firm. We combined passion for success in the global business arena with hands-on experience to help foreign companies navigate the entry into U.S. markets and U.S. companies in initiating and expanding exports to foreign markets.</p>
</section>

<h2 class="section-title" style="top:930px">ABOUT <em>HARBOR ADVISORY</em></h2>
<div class="divider" style="top:995px"></div>
<p class="lead">Mara Velinska has ten years of experience in economic development, foreign direct investment (FDI) and trade.</p>
<p class="about-intro">Prior to founding TW Harbor Advisory, she worked as Director of Global Business Development – Europe at the Ridgeview State Development Commission (RSDC) assisting European companies to expand in the state. While at the RSDC, Mara participated in a number of international trade shows and organized multiple investment and trade missions for the state's governors.</p>

<div class="portrait"><div role="img" aria-label="Portrait photo of the firm's founder"></div></div>
<div class="bio">
  <p>Mara was appointed by the U.S. Secretary of Commerce to the Ridgeview District Export Council (RDEC), an organization of business leaders whose expertise in international business provides a source of professional advice for the region's firms. She was elected to serve as the RDEC Vice Chair in 2017. Mara is a speaker at the Trade Academy, an RDEC program providing export training and education. She will teach an International Business Management class at Ridgeview State University during the fall semester of 2017.</p>
  <p>Mara serves as the first ever Czech Honorary Consul for the State of Ridgeview. With her strong network on both sides of the Atlantic, Mara supports bilateral economic and trade relations between the Czech Republic, the European Union and the United States.</p>
  <p>Passionate about her community, Mara has joined several non-profit boards and organizations, including the Oakhaven Cancer Institute Foundation Board, the Harbor Leadership Institute, the Civic Service Club, the Ridgeview Women's Leadership Forum, the Network of Women in Global Trade, and the Whitcombe Scholars Alumni Board.</p>
  <p>Mara is a 2005 honors MBA graduate of Ridgeview State University. She obtained her undergraduate BA degree in finance and international business from the same institution. She is a member of the Leadership Ridgeview Class XI and the Leadership Greater Millbrook Class XXVI. Mara is fluent in English and Czech. She also speaks <strong>German and Slovakian.</strong></p>
</div>

<div class="services-band"></div>
<h2 class="section-title" style="top:1768px">OUR <em>SERVICES</em></h2>
<div class="divider on-grey" style="top:1830px"></div>

<section class="panel blue" style="left:0;top:1885px">
  <h3>Exports assists U.S. companies with their export initiatives by</h3>
  <hr>
  <ul>
    <li>Identifying and developing new customer relationships in foreign markets</li>
    <li>Organizing trade mission trips</li>
    <li>Coordinating successful trade show visits</li>
    <li>Providing an assistance with the completion of a strategic export plan</li>
    <li>Finding additional resources to support and grow companies' exports</li>
    <li>Connecting companies with other international trade experts to further support their international logistics, payment &amp; financing management, and to address any trade regulations and legal issues</li>
  </ul>
</section>
<div class="panel photo-meeting" style="left:600px;top:1885px" role="img" aria-label="Photo of business partners shaking hands across a desk"></div>

<div class="panel photo-tablet" style="left:0;top:2370px" role="img" aria-label="Photo of hands holding a tablet showing business charts"></div>
<section class="panel blue" style="left:600px;top:2370px;padding-left:34px">
  <h3>FDI assists international companies with navigating the entry into U.S. markets by</h3>
  <hr>
  <ul>
    <li>Managing the site selection process</li>
    <li>Collecting market data</li>
    <li>Site identification and analysis</li>
    <li>Providing an appraisal of proposed incentives and financing assistance</li>
    <li>Management of the documentation process</li>
  </ul>
</section>

<div class="grey-gap"></div>

<footer class="footer">
  <h4 style="left:183px">DROP US A LINE</h4>
  <div class="field" style="top:72px;height:34px">Name</div>
  <div class="field" style="top:116px;height:34px">Email</div>
  <div class="field" style="top:150px;height:58px;margin-top:10px">Message</div>
  <div class="send">SEND</div>

  <h4 style="left:505px">LOCATION MAP</h4>
  <div class="map" role="img" aria-label="Street map showing the office location"></div>

  <h4 style="left:858px">FIND US</h4>
  <div class="contact" style="top:70px">
    <svg width="14" height="18" viewBox="0 0 14 18"><path d="M7 0a7 7 0 0 0-7 7c0 5 7 11 7 11s7-6 7-11a7 7 0 0 0-7-7zm0 10a3 3 0 1 1 0-6 3 3 0 0 1 0 6z" fill="#fff"/></svg>
    <span>TW Harbor Advisory, LLC</span><span>Mara Velinska, MBA</span><span>President</span>
  </div>
  <div class="contact" style="top:134px">
    <svg width="15" height="15" viewBox="0 0 16 16"><path d="M3 1l3 3-2 2c1 2 4 5 6 6l2-2 3 3-2 2C7 15 1 9 1 3z" fill="#fff"/></svg>
    <span style="font-size:15px">+1 (555) 014-0288</span>
  </div>
  <div class="contact" style="top:175px">
    <svg width="15" height="12" viewBox="0 0 16 12"><rect x="0.5" y="0.5" width="15" height="11" fill="none" stroke="#fff"/><path d="M1 1l7 6 7-6" fill="none" stroke="#fff"/></svg>
    <span>info@twharboradvisory.example</span>
  </div>
  <div class="social" style="left:858px"></div>
  <div class="social" style="left:892px"></div>
  <div class="social" style="left:926px"></div>
  <div class="social" style="left:960px"></div>
</footer>
<div class="copyright">© Copyright 2016 by TW Harbor Advisory, LLC.</div>

</body>
</html>
```